11/06/2017 Brochure

Local Internet service provider, www.tallowridge-link.com I have attached a quick edit of one of our previous versions to give you an idea of what words we want on the brochures.

Industry/Entity Type

Internet Service Provider

Colors

Designer to choose colors to be used in the design.

Requirements
Must have
• All words in the attached basic brochure
Nice to have
• Pictures related to the internet

```html
<!DOCTYPE html>
<html lang="en">
<head>
<meta charset="utf-8">
<title>Tallowridge Link – Business Internet Brochure</title>
<link href="https://fonts.googleapis.com/css2?family=Open+Sans:ital,wght@0,400;0,600;0,700;0,800;1,600;1,700&display=swap" rel="stylesheet">
<style>
:root{
  --orange:#f05a1c;
  --orange-deep:#e6420a;
  --charcoal:#3d3d40;
  --paper:#ffffff;
  --mist:#efefef;
  --ink:#4a4a4a;
}
*{box-sizing:border-box;margin:0;padding:0}
html,body{width:1200px;height:800px;overflow:hidden;background:var(--paper)}
body{font-family:"Open Sans",Arial,sans-serif;color:var(--ink)}
.brochure{position:relative;width:1200px;height:800px;display:flex}

/* ---------- pricing panel ---------- */
.panel-pricing{width:400px;height:800px;background:var(--charcoal);padding:26px 40px 20px;display:flex;flex-direction:column;gap:14px}
.tier{position:relative}
.tier-tab{display:block;width:90px;margin:0 auto;background:var(--orange);color:#fff;text-align:center;font-weight:800;font-size:12px;border-radius:8px 8px 0 0;padding:1px 0}
.rate-table{width:100%;border-collapse:collapse;background:#fff;border:2px solid var(--orange);border-radius:6px;overflow:hidden;font-weight:700;font-size:12px;text-align:center;color:#333}
.rate-table th{color:var(--orange);font-size:8px;line-height:9px;font-weight:800;padding:2px 0;border-bottom:2px solid var(--orange)}
.rate-table td{height:18px;border-bottom:1.5px solid var(--orange)}
.rate-table th+th,.rate-table td+td{border-left:2px solid var(--orange)}
.rate-table tr:last-child td{border-bottom:none}
.rate-table.is-featured{background:var(--orange);color:#fff;border-color:#fff}
.rate-table.is-featured th{color:#fff;border-bottom-color:#fff}
.rate-table.is-featured td{border-bottom-color:#fff}
.rate-table.is-featured th+th,.rate-table.is-featured td+td{border-left-color:#fff}

/* ---------- inner spread ---------- */
.spread{position:relative;width:800px;height:800px}
.spread-bg{position:absolute;inset:0}
.panel-intro,.panel-contact{position:absolute;top:0;width:400px;height:800px}
.panel-intro{left:0}
.panel-contact{left:400px}

.headline-pill{position:absolute;left:28px;top:42px;width:344px;background:var(--orange);color:#fff;border-radius:22px;text-align:center;font-weight:800;font-size:17px;line-height:20px;padding:9px 10px;text-transform:uppercase}
.intro-copy{position:absolute;left:36px;top:124px;width:330px;font-size:12.5px;line-height:21px;text-align:justify;color:#555}

.faq-pill{position:absolute;left:60px;top:486px;width:280px;border:2px solid #fff;border-radius:26px;color:#fff;text-align:center;font-weight:700;font-size:17px;padding:9px 0}
.faq{color:#fff;font-size:12px;line-height:17px}
.faq dt{font-weight:700;font-style:italic}
.faq dd{margin-bottom:14px}
.faq-left{position:absolute;left:36px;top:548px;width:330px}
.faq-right{position:absolute;left:30px;top:408px;width:340px}

.packages-pill{position:absolute;left:30px;top:30px;width:340px;background:var(--charcoal);color:#fff;border-radius:24px;text-align:center;text-transform:uppercase;font-weight:800;padding:7px 0}
.packages-pill strong{display:block;font-size:15px;line-height:18px}
.packages-pill span{display:block;font-size:10.5px;line-height:13px}
.call-title{position:absolute;left:0;top:98px;width:400px;text-align:center;font-size:24px;font-weight:800;color:#444}
.call-icon{position:absolute;left:186px;top:134px;width:28px;height:28px}
.area-list{position:absolute;left:62px;top:172px;width:276px;list-style:none;display:flex;flex-direction:column;gap:7px}
.area-list li{border:2px solid #444;border-radius:22px;text-align:center;font-weight:700;font-size:12.5px;line-height:15px;padding:3px 0;color:#333;background:var(--mist)}

.contact-pill{position:absolute;left:30px;top:626px;width:340px;background:#fff;color:var(--orange);border-radius:22px;text-align:center;text-transform:uppercase;font-weight:800;font-size:11.5px;line-height:15px;padding:8px 14px}
.contact-phone{position:absolute;left:0;top:690px;width:400px;text-align:center;color:#fff;font-size:34px;font-weight:800;letter-spacing:.5px}
</style>
</head>
<body>
<main class="brochure">

  <section class="panel-pricing" aria-label="Package pricing">
    <div class="tier">
      <span class="tier-tab">TIER 1</span>
      <table class="rate-table">
        <tr><th>DOWNLOAD<br>SPEED</th><th>UPLOAD<br>SPEED</th></tr>
        <tr><td>10 Mb</td><td>10 Mb</td></tr>
        <tr><td>20 Mb</td><td>20 Mb</td></tr>
        <tr><td>30 Mb</td><td>30 Mb</td></tr>
        <tr><td>40 Mb</td><td>40 Mb</td></tr>
        <tr><td>50 Mb</td><td>50 Mb</td></tr>
        <tr><td>60 Mb</td><td>60 Mb</td></tr>
        <tr><td>70 Mb</td><td>70 Mb</td></tr>
        <tr><td>80 Mb</td><td>80 Mb</td></tr>
        <tr><td>90 Mb</td><td>90 Mb</td></tr>
        <tr><td>100 Mb</td><td>100 Mb</td></tr>
      </table>
    </div>
    <div class="tier">
      <span class="tier-tab">TIER 2</span>
      <table class="rate-table">
        <tr><th>DOWNLOAD<br>SPEED</th><th>UPLOAD<br>SPEED</th></tr>
        <tr><td>10 Mb</td><td>5 Mb</td></tr>
        <tr><td>20 Mb</td><td>10 Mb</td></tr>
        <tr><td>30 Mb</td><td>15 Mb</td></tr>
        <tr><td>40 Mb</td><td>20 Mb</td></tr>
        <tr><td>50 Mb</td><td>25 Mb</td></tr>
        <tr><td>60 Mb</td><td>30 Mb</td></tr>
        <tr><td>70 Mb</td><td>35 Mb</td></tr>
        <tr><td>80 Mb</td><td>40 Mb</td></tr>
        <tr><td>90 Mb</td><td>45 Mb</td></tr>
        <tr><td>100 Mb</td><td>50 Mb</td></tr>
      </table>
    </div>
    <div class="tier">
      <span class="tier-tab">TIER 3</span>
      <table class="rate-table is-featured">
        <tr><th>DOWNLOAD<br>SPEED</th><th>UPLOAD<br>SPEED</th><th>PRICE<br>PER MONTH</th></tr>
        <tr><td>1 Mb</td><td>768 Kb</td><td>$40</td></tr>
        <tr><td>2 Mb</td><td>1024 Kb</td><td>$50</td></tr>
        <tr><td>4 Mb</td><td>1280 Kb</td><td>$60</td></tr>
        <tr><td>6 Mb</td><td>1536 Kb</td><td>$70</td></tr>
        <tr><td>8 Mb</td><td>1746 Kb</td><td>$80</td></tr>
        <tr><td>10 Mb</td><td>2048 Kb</td><td>$90</td></tr>
        <tr><td>12 Mb</td><td>2048 Kb</td><td>$100</td></tr>
      </table>
    </div>
  </section>

  <section class="spread">
    <svg class="spread-bg" width="800" height="800" viewBox="0 0 800 800" aria-hidden="true">
      <defs>
        <linearGradient id="orangeFill" x1="0" y1="0" x2="1" y2="1">
          <stop offset="0" stop-color="#f36a25"/>
          <stop offset="1" stop-color="#e6420a"/>
        </linearGradient>
        <path id="visitPath" d="M0,500 C200,400 500,390 800,340"/>
      </defs>
      <rect x="0" y="0" width="400" height="800" fill="#ffffff"/>
      <rect x="400" y="0" width="400" height="800" fill="#efefef"/>
      <path d="M0,484 C200,384 500,374 800,324 L800,800 L0,800 Z" fill="url(#orangeFill)"/>
      <path d="M0,470 C200,370 500,360 800,310" fill="none" stroke="#3d3d40" stroke-width="7"/>
      <text font-family="Open Sans, Arial, sans-serif" font-size="11.5" font-weight="600" fill="#ffffff">
        <textPath href="#visitPath" startOffset="40">Visit tallowridge-link.com to see our service area and view other internet packages available in your area.</textPath>
      </text>
    </svg>

    <div class="panel-intro">
      <h2 class="headline-pill">We have a variety of<br>packages to suit your needs</h2>
      <p class="intro-copy">Increasing employee productivity by reducing the extended internet wait times can be your first step to increased profits… Each business utilizes the internet differently, some reach locally and others reach globally; we work with all of our customers to have the correct speed and connectivity that meets their needs and requirements. Those same requirements are revised regularly to keep pace with constantly changing and developing business environments.</p>

      <h3 class="faq-pill">Frequently Asked Questions</h3>
      <dl class="faq faq-left">
        <dt>Isn't satellite the fastest?</dt>
        <dd>No. Typical latency with satellite service is between 900–1200ms. Enjoy the stability of our network consistently 50ms or less.</dd>
        <dt>Can I use an internet based phone system?</dt>
        <dd>Yes! VoIP, as it is called, does work with our service as our service is low jitter and works extremely well. Some examples are Voxline, TalkCube, Ringwise, ChatPort and more.</dd>
        <dt>What is the commitment period for the service contract?</dt>
        <dd>No contract is required for internet service.</dd>
      </dl>
    </div>

    <div class="panel-contact">
      <h2 class="packages-pill"><strong>Business Packages</strong><span>with speeds exceeding 100 Mbps</span></h2>
      <p class="call-title">CALL TODAY!</p>
      <svg class="call-icon" viewBox="0 0 28 28" aria-hidden="true">
        <circle cx="14" cy="14" r="12.5" fill="none" stroke="#444" stroke-width="2"/>
        <path d="M9 8.5c.6-.6 1.4-.6 1.9 0l1.4 1.7c.4.5.3 1.2-.1 1.6l-.8.7c.7 1.5 1.9 2.8 3.4 3.5l.7-.8c.4-.4 1.1-.5 1.6-.1l1.7 1.4c.6.5.6 1.3 0 1.9l-.9.9c-.9.9-2.4 1-3.6.3-2.5-1.4-4.5-3.4-5.900-5.9-.7-1.2-.6-2.7.3-3.6z" fill="#444"/>
      </svg>
      <ul class="area-list">
        <li>Reno, Carson, Dayton, VC<br>775-555-0140</li>
        <li>Mason Valley Area<br>775-555-0163</li>
        <li>Smith Valley Area<br>775-555-0178</li>
      </ul>

      <dl class="faq faq-right">
        <dt>Will my gaming work well with this service?</dt>
        <dd>Yes! We have a very low latency specifically designed for real time action. Low latency equals better gaming performance.</dd>
        <dt>How can I verify the speed I am getting from my current provider?</dt>
        <dd>Several on-line services provide speed tests to check actual performance. We use pacerate.net/speedtest because we have found it to be the most accurate.</dd>
      </dl>

      <p class="contact-pill">Contact one of our business specialists to develop a customized quote to meet your business's specific needs today.</p>
      <p class="contact-phone">775-555-0192</p>
    </div>
  </section>

</main>
</body>
</html>
```